Microsoft Word Sales Proposal Template

We'd like to produce a standard sales proposal template for Microsoft Word that better represents our company than our current template. Right now we have a very basic, dated look and feel to our template. We would like a proposal that graphically reflects our current branding, cleanly communicates the information contained in the proposal, and keeps the reader visually engaged with the text.

Our proposal documents consistently include the following hierarchy of information. We’d like a template designed to be flexible to change in this hierarchy, with a focus on cohesive design elements (heading fonts and styling, etc.):

- Cover Page
- Table of Contents
- Executive Summary
- Project Approach
- Sample Work/Select Clients List
- About Pelham Brook
- References
- Project Milestones and Budget
- Appendices

The primary focus is on the visual design elements: headers and footers, fonts, heading design consistency, and other graph and visual elements reflected in the attached proposal samples.

The Pelham Brook logo should not be altered in any way. I have attached 2 acceptable logos for use in the document. Client logos should also not be altered in any way. Placeholders for client logos in the template are appreciated for speed and accuracy of placement. Please avoid using cheesy stock photos.

For more information about our company and to review our current aesthetic, please visit http://www.pelhambrook-co.net/.
Updates

Thanks to everyone who has saved the project. We're excited to see your work. Please reach out if you need any clarifications or have questions.

Target Market(s)

Employees at large nonprofits who are responsible for technology decisions. Also target employees who create content and manage content for nonprofits.

Industry/Entity Type

It Company

Font styles to use
Serif
Sans Serif

Requirements
Must have
• Must Have:
• - Sample Table of Content
• - Representation of Section Headings
• - Clean design representative of our brand
• - Template elements that appropriately reflect each potential Table of Contents item
• - Easy flow of reading
• - Templates for reusable graphs and tables
• - Include 'Proprietary and Confidential' somewhere in footer to denote the confidentiality of proposal information
Should not have
• - cheesy stock images

```html
<!DOCTYPE html>
<html lang="en">
<head>
<meta charset="utf-8">
<title>About Company – Pelham Brook</title>
<link href="https://fonts.googleapis.com/css2?family=Roboto+Condensed:wght@300;400;700&display=swap" rel="stylesheet">
<style>
  :root {
    --navy: #0c2540;
    --navy-deep: #081b30;
    --accent-blue: #1e8fe0;
    --rule-blue: #4fa9e0;
    --rule-orange: #e98a2a;
    --paper: #e4e4e4;
    --body-text: #8a8a8a;
    --white: #ffffff;
  }
  * { margin: 0; padding: 0; box-sizing: border-box; }
  html, body { width: 927px; height: 1200px; overflow: hidden; }
  body {
    font-family: "Roboto Condensed", "Arial Narrow", sans-serif;
    background: var(--paper);
  }
  .page {
    position: relative;
    width: 927px;
    height: 1200px;
    background: var(--paper);
    overflow: hidden;
  }
  .page-header {
    position: absolute;
    left: 0; top: 0;
    width: 100%;
    height: 70px;
    background: linear-gradient(180deg, var(--navy) 0%, var(--navy-deep) 100%);
    border-bottom: 3px solid var(--rule-blue);
    box-shadow: 0 2px 0 #ffffff;
  }
  .page-title {
    position: absolute;
    left: 21px; top: 12px;
    font-size: 34px;
    font-weight: 700;
    letter-spacing: -0.3px;
    color: var(--white);
  }
  .page-title .lead { color: var(--accent-blue); }
  .brand {
    position: absolute;
    right: 20px; top: 17px;
    display: flex;
    align-items: center;
    gap: 9px;
    color: var(--white);
    font-size: 27px;
    font-weight: 400;
  }
  .brand-dot { width: 40px; height: 40px; }
  .content {
    position: absolute;
    left: 23px; top: 103px;
    width: 876px;
  }
  .section-heading {
    font-size: 25px;
    font-weight: 700;
    color: var(--accent-blue);
    margin-bottom: 8px;
  }
  .content p {
    font-size: 18.4px;
    font-weight: 300;
    letter-spacing: 0.1px;
    line-height: 33px;
    color: #7e7e7e;
    text-align: justify;
    margin-bottom: 33px;
  }
  .content p.short { text-align: left; }
  .page-footer {
    position: absolute;
    left: 0; bottom: 0;
    width: 100%;
    height: 62px;
    background: linear-gradient(180deg, var(--navy) 0%, var(--navy-deep) 100%);
    border-top: 3px solid var(--rule-orange);
    box-shadow: 0 -3px 0 #ffffff, 0 -5px 0 var(--rule-orange);
  }
  .footer-url {
    position: absolute;
    left: 18px; top: 21px;
    font-size: 18px;
    color: var(--white);
  }
  .page-number {
    position: absolute;
    right: 14px; top: 21px;
    font-size: 18px;
    font-weight: 700;
    color: var(--accent-blue);
  }
</style>
</head>
<body>
<div class="page">
  <header class="page-header">
    <h1 class="page-title"><span class="lead">About</span> Company</h1>
    <div class="brand">
      <svg class="brand-dot" viewBox="0 0 40 40" aria-hidden="true"><circle cx="20" cy="20" r="19" fill="#3a8fd0"/></svg>
      <span>pelhambrook</span>
    </div>
  </header>

  <main class="content">
    <h2 class="section-heading">About Text</h2>
    <p>This template uses a few tables to create the page structure that follows. A host table consisting of just two columns and one row enables the sidebar content to sit beside the text, tables, and diagram on the left without any complicated positioning required. Nested tables (a nested table is just one table inside another) in both the left and right column enable you to place text beside the process graphic, provide the small financial table below left, and provide the side-bar table with a separate cell for the heading text.</p>
    <p>This template uses a few tables to create the page structure that follows. A host table consisting of just two columns and one row enables the sidebar content to sit beside the text, tables, and diagram on the left without any complicated positioning required. Nested tables (a nested table is just one table inside another) in both the left and right column enable you to place text beside the process graphic, provide the small financial table below left, and provide the side-bar table with a separate cell for the heading text.</p>
    <p>&nbsp;tables, and diagram on the left without any complicated positioning required. Nested tables (a nested table is just one table inside another) in both the left and right column enable you to place text beside the process graphic</p>
    <p class="short">provide the small financial table below left, and provide the sidebar table with a separate cell for the heading text.</p>
    <p>This template uses a few tables to create the page structure that follows. A host table consisting of just two columns and one row enables the sidebar content to sit beside the text, tables, and diagram on the left without any complicated positioning required. Nested tables (a nested table is just one table inside another) in both the left and right column enable you to place text beside the process graphic, provide the small financial table below left, and provide the side-bar table with a separate cell for the heading text.</p>
  </main>

  <footer class="page-footer">
    <span class="footer-url">www.pelhambrook-co.net</span>
    <span class="page-number">Page : 01</span>
  </footer>
</div>
</body>
</html>
```